Therapy Dog Business need a brochure

I need a brochure designed for my Canine Assisted Therapy business in Victoria Australia. I have a logo already and info and photos to upload.
Best as white background and using the colours from the logo please
Updates

Hi Everyone,
I am sorry to have to revise the brief. I have added three new photos I was unable to add due to the size. I have had to wait for my photographer to change the size to add them today. I have been really inspired by all the work you have done so far. Thank you.
Could you please add the following on the brochure. (Under the individual dogs photo)
1. Juniper is the white dog. Please add the following under her picture. Juniper is one of the first Court Dogs in Australia. Working in Victoria, she has worked in the following Courts. The Ostrander Inquest Bench, The Dunmore Justice Hall in Collingwood, and the Brackwell Tribunal in Melbourne CBD. Her ability to use her intuition for clients is inspiring. Please contact us for potential use in Courts. Juniper has worked at the Harrowgate Safety College, and at STAVE at Har Saf. She is a stunning dog!
2. Barnaby is the golden dog. Barnaby is Junipers son, and had her instinct of intuition of who needs his help. Barnaby has an incredible soft approach as does his mother Juniper. He is incredibly safe with young children, and yet has a playful nature for adolescents and adults alike. He is soft and caring, and like his mother will go to those who need him most. Barnaby like his mother has worked at Harrowgate Safety, his time at HS included the Harrowgate Safety Council (HSC) Both he and his mother have very impressive CV'S!
3. Pepper the black dog. Pepper is my Therapy and Assistance dog "trainer" she is safe and stable with all the dogs and people I train for Therapy Dog Training and Assistance Dog Training. She has also been with me on my journey as a Counsellor and I have been able to work alongside her and Juniper for Counselling sessions.
She is soft, caring, and also intuitive. I am incredibly grateful for her help, as well as Juniper and Barnaby.
ALSO I am so sorry to add this but could you also add the following: Maybe in dot point?
Court Dog Availability
Therapy Dog Visits - Lawyers - Courts - Child Protection
Police Station / Ambulance Station / Fire Station - Visits
Private Therapy Dog Sessions
website and email confirmation coming soon. Thank you

3. Pepper the black dog.

Target Market(s)

First Responders

Requirements
Must have
• All the photos provided.
Should not have
• Generic photos

```html
<!DOCTYPE html>
<html lang="en">
<head>
<meta charset="utf-8">
<title>Tails of Comfort – Canine Assisted Therapy Brochure</title>
<link href="https://fonts.googleapis.com/css2?family=Rubik:wght@500;600;800&family=Figtree:wght@400;500&family=Caveat:wght@700&display=swap" rel="stylesheet">
<style>
:root{
  --stage:#c9c9c9;
  --maroon:#5a1c26;
  --maroon-deep:#4e1620;
  --rust:#b4542e;
  --orange:#eba35a;
  --pill:#c6622f;
  --cream:#fbeee1;
  --white:#ffffff;
}
*{margin:0;padding:0;box-sizing:border-box}
html,body{width:1200px;height:785px;overflow:hidden;background:var(--stage)}
body{position:relative;font-family:"Figtree",Arial,sans-serif;color:var(--cream)}
.page{position:absolute;overflow:hidden}
.page-front{left:61px;top:47px;width:528px;height:684px;
  background:linear-gradient(180deg,var(--rust) 0%,#a9492d 35%,#6e2528 70%,var(--maroon) 100%)}
.page-back{left:624px;top:47px;width:526px;height:682px;
  background:linear-gradient(180deg,var(--rust) 0%,#9c4330 40%,#6b2429 72%,var(--maroon) 100%)}
.abs{position:absolute}
.photo{position:absolute}

/* front */
.photo-puppy{left:0;top:0;width:250px;height:200px;
  background:radial-gradient(ellipse at 45% 40%,#c9a37e 0%,#b5784e 40%,rgba(180,84,46,0) 78%),linear-gradient(135deg,#3d8a86 0%,#b4542e 70%)}
.intro-panel{left:231px;top:0;width:297px;height:167px;background:var(--maroon);
  border-bottom-left-radius:42px;border-bottom:2px solid var(--orange);border-left:2px solid var(--orange)}
.brand-badge{left:168px;top:34px;width:106px;height:106px;border-radius:50%;background:var(--white);
  display:flex;align-items:center;justify-content:center;text-align:center;
  font-family:"Rubik",sans-serif;font-weight:600;font-size:12px;line-height:14px;color:var(--maroon)}
.h-intro{left:287px;top:22px;font-family:"Rubik",sans-serif;font-weight:600;font-size:17px;line-height:24px;color:var(--white)}
.h-intro span{color:var(--orange)}
.body-small{font-size:8.3px;line-height:10.4px;color:var(--cream)}
.p-intro{left:287px;top:73px;width:235px}
.h-section{font-family:"Rubik",sans-serif;font-weight:600;font-size:16.5px;line-height:21px;color:var(--white)}
.h-benefits{left:31px;top:161px}
.h-why{left:278px;top:184px}
.item-title{font-family:"Rubik",sans-serif;font-weight:500;font-size:11.5px;color:var(--white);display:flex;align-items:center;gap:6px}
.item-title::before{content:"";width:16px;height:16px;border-radius:50%;background:var(--white);flex:none}
.photo-dogs{left:0;top:480px;width:528px;height:204px;
  background:linear-gradient(180deg,#9fb1e4 0%,#8ea2da 100%);border-top-left-radius:60px 30px}
.photo-black-dog{left:395px;top:410px;width:132px;height:235px;border-radius:60px 60px 0 0;
  background:linear-gradient(180deg,#2a2426 0%,#151113 100%)}
.cta-band{left:0;top:594px;width:504px;height:90px;background:var(--orange);border-top-right-radius:40px}
.h-cta{left:31px;top:600px;font-family:"Rubik",sans-serif;font-weight:800;font-size:17px;color:var(--maroon)}
.p-cta{left:31px;top:626px;width:450px;font-size:7.9px;line-height:10.3px;color:var(--white);font-weight:500}
.contact-row{display:flex;align-items:center;font-family:"Rubik",sans-serif;font-weight:500;color:var(--white);white-space:nowrap}
.contact-row .ci{display:flex;align-items:center;gap:5px}
.contact-row svg{flex:none}
.contacts-front{left:32px;top:658px;font-size:10px;gap:22px}

/* back */
.dog-frame{position:absolute;width:172px;height:156px;background:var(--maroon-deep);border-radius:36px 6px 36px 6px;padding:8px}
.dog-photo{width:100%;height:100%;border-radius:6px 28px 6px 28px}
.frame-juniper{left:35px;top:31px}
.frame-barnaby{left:324px;top:190px}
.frame-pepper{left:35px;top:366px}
.photo-white{background:linear-gradient(160deg,#8da3dc 0%,#e8dcc7 45%,#f2ebdf 60%,#8ea2da 100%)}
.photo-golden{background:linear-gradient(160deg,#d4633f 0%,#9cb0e2 30%,#ead9bd 55%,#8ea2da 100%)}
.photo-black{background:linear-gradient(180deg,#d99a5a 0%,#9fb1e4 20%,#1c1719 55%,#8ea2da 100%)}
.dog-name{font-family:"Caveat",cursive;font-weight:700;font-size:40px;line-height:40px;color:var(--white)}
.dog-bio{font-size:9.9px;line-height:12.4px;color:var(--cream)}
.name-juniper{left:224px;top:40px}
.bio-juniper{left:224px;top:82px;width:285px}
.name-barnaby{left:39px;top:200px}
.bio-barnaby{left:39px;top:241px;width:280px}
.name-pepper{left:224px;top:374px}
.bio-pepper{left:224px;top:416px;width:285px}
.availability-pill{left:42px;top:538px;width:463px;height:31px;border-radius:16px;background:var(--pill);
  display:flex;align-items:center;justify-content:center;font-family:"Rubik",sans-serif;font-weight:500;font-size:17.5px;color:var(--cream)}
.availability-row{left:0;width:526px;display:flex;justify-content:center;align-items:center;gap:9px;
  font-family:"Rubik",sans-serif;font-weight:500;font-size:11px;color:var(--cream)}
.row-1{top:578px}
.row-2{top:594px}
.tick{display:inline-flex;align-items:center;gap:4px}
.sep{opacity:.9}
.footer-band{left:0;top:641px;width:526px;height:41px;background:var(--maroon-deep)}
.rule{left:0;top:640px;width:526px;height:1px;background:var(--cream)}
.private-title{left:0;top:631px;width:526px;display:flex;justify-content:center}
.private-title span{background:#5c1d27;padding:0 8px;font-family:"Rubik",sans-serif;font-weight:600;font-size:12.5px;color:var(--cream);display:flex;align-items:center;gap:6px}
.private-title span::before,.private-title span::after{content:"";width:4px;height:4px;border-radius:50%;background:var(--orange)}
.contacts-back{left:0;width:526px;justify-content:center;top:654px;font-size:10.5px;gap:18px;color:var(--cream)}
</style>
</head>
<body>

<section class="page page-front">
  <div class="photo photo-puppy" role="img" aria-label="Photo of a brown and white puppy placing its paw in a person's hand"></div>
  <div class="abs intro-panel"></div>
  <div class="abs brand-badge">Tails of<br>Comfort</div>

  <h1 class="abs h-intro">What is Canine<br><span>Assisted Therapy?</span></h1>
  <p class="abs body-small p-intro">Canine Assisted Therapy (CAT) is a unique form of therapy that integrates trained therapy dogs into the healing process. By working alongside licensed therapists, these compassionate and well-trained dogs help support individuals in overcoming emotional, physical, and psychological challenges.&nbsp; This innovative approach promotes healing, reduces stress, and enhances overall well-being.</p>

  <h2 class="abs h-section h-benefits">Benefits of<br>Canine Assisted Therapy</h2>

  <h3 class="abs item-title" style="left:31px;top:216px">Emotional Support and Comfort</h3>
  <p class="abs body-small" style="left:34px;top:243px;width:215px">Therapy dogs provide immediate emotional support, offering comfort and companionship during therapy sessions.&nbsp; Their calming presence helps reduce feelings of anxiety, stress, and depression, and grief, creating a safe and nurturing environment for healing.</p>

  <h3 class="abs item-title" style="left:31px;top:303px">Stress Relief and Relaxation</h3>
  <p class="abs body-small" style="left:34px;top:329px;width:230px">Interacting with dogs has been proven to reduce cortisol (stress hormone) levels and increase serotonin and oxytocin, the “feel-good” hormones.&nbsp; This natural relief from stress makes Canine Assisted Therapy an ideal option for individuals dealing with anxiety, trauma, PTSD, and grief,</p>

  <h3 class="abs item-title" style="left:31px;top:390px">Improved Mental Health</h3>
  <p class="abs body-small" style="left:34px;top:416px;width:238px">Therapy dogs encourage social interaction, communication, and emotional expression, helping individuals address mental health challenges such as depression, anxiety, PTSD, and grief.&nbsp; The unconditional love and companionship of a dog can foster trust and openness during therapy sessions.</p>

  <h2 class="abs h-section h-why">Why Choose<br>Canine Assisted Therapy?</h2>

  <h3 class="abs item-title" style="left:278px;top:239px">Proven Effectiveness</h3>
  <p class="abs body-small" style="left:281px;top:265px;width:235px">Studies and testimonials highlight the positive effects therapy dogs have on emotional, psychological and physical health.</p>

  <h3 class="abs item-title" style="left:278px;top:298px">Non-Invasive and Gentle</h3>
  <p class="abs body-small" style="left:281px;top:323px;width:230px">Therapy dogs provide a natural and non-threatening way to engage with patients, making it accessible for individuals who may feel apprehensive about traditional therapy methods.</p>

  <h3 class="abs item-title" style="left:278px;top:374px">Safe and Trustworthy</h3>
  <p class="abs body-small" style="left:281px;top:400px;width:195px">All therapy dogs are carefully trained to work with professionals, ensuring<br>that interactions are safe,<br>beneficial, and appropriate<br>for all individuals</p>

  <div class="photo photo-dogs" role="img" aria-label="Photo of two pale Labradors lying on a blue blanket"></div>
  <div class="photo photo-black-dog" role="img" aria-label="Photo of a black Labrador sitting upright"></div>

  <div class="abs cta-band"></div>
  <h2 class="abs h-cta">Join the Healing Journey Today!</h2>
  <p class="abs p-cta">Whether you are seeking emotional support or mental health improvement, Canine Assisted Therapy offers a unique and compassionate approach to healing.&nbsp; Connect with us today to learn more about how a therapy dog can help enhance your life and well-being.</p>
  <div class="abs contact-row contacts-front">
    <span class="ci"><svg width="10" height="10" viewBox="0 0 24 24"><path fill="#fff" d="M6.6 10.8a15 15 0 0 0 6.6 6.6l2.2-2.2c.3-.3.7-.4 1-.2 1.1.4 2.3.6 3.6.6.6 0 1 .4 1 1V20c0 .6-.4 1-1 1A17 17 0 0 1 3 4c0-.6.4-1 1-1h3.5c.6 0 1 .4 1 1 0 1.3.2 2.5.6 3.6.1.3 0 .7-.2 1z"/></svg>0400 123 456</span>
    <span class="ci"><svg width="12" height="9" viewBox="0 0 24 17"><rect x="1" y="1" width="22" height="15" fill="none" stroke="#fff" stroke-width="1.6"/><path d="M1 1l11 9 11-9" fill="none" stroke="#fff" stroke-width="1.6"/></svg>hello@tailsofcomfort.example</span>
    <span class="ci"><svg width="11" height="11" viewBox="0 0 24 24" fill="none" stroke="#fff" stroke-width="1.6"><circle cx="12" cy="12" r="10"/><ellipse cx="12" cy="12" rx="4.5" ry="10"/><path d="M2 12h20M4 6.5h16M4 17.5h16"/></svg>www.tailsofcomfort.example</span>
  </div>
</section>

<section class="page page-back">
  <div class="dog-frame frame-juniper"><div class="dog-photo photo-white" role="img" aria-label="Photo of Juniper, a white Labrador lying on a blue blanket"></div></div>
  <h2 class="abs dog-name name-juniper">Juniper</h2>
  <p class="abs dog-bio bio-juniper">Juniper is one of the first Court Dogs in Australia. Working in Victoria, she has worked in the following Courts. The Ostrander Inquest Bench, The Dunmore Justice Hall in Collingwood, and the Brackwell Tribunal in Melbourne CBD. Her ability to use her intuition for clients is inspiring. Please contact us for potential use in Courts. Juniper has worked at the Harrowgate Safety College, and at STAVE at Har Saf. She is a stunning dog!</p>

  <h2 class="abs dog-name name-barnaby">Barnaby</h2>
  <p class="abs dog-bio bio-barnaby">Barnaby is Junipers son, and had her instinct of intuition of who needs his help. Barnaby has an incredible soft approach as does his mother Juniper. He is incredibly safe with young children, and yet has a playful nature for adolescents and adults alike. He is soft and caring, and like his mother will go to those who need him most. Barnaby like his mother has worked at Harrowgate Safety, his time at HS included the Harrowgate Safety Council (HSC) Both he and his mother have very impressive CV'S!</p>
  <div class="dog-frame frame-barnaby"><div class="dog-photo photo-golden" role="img" aria-label="Photo of Barnaby, a golden Labrador lying on a blue blanket beside an orange cushion"></div></div>

  <div class="dog-frame frame-pepper"><div class="dog-photo photo-black" role="img" aria-label="Photo of Pepper, a black Labrador lying on a blue blanket"></div></div>
  <h2 class="abs dog-name name-pepper">Pepper</h2>
  <p class="abs dog-bio bio-pepper">Pepper is my Therapy and Assistance dog "trainer" she is safe and stable with all the dogs and people I train for Therapy Dog Training and Assistance Dog Training. She has also been with me on my journey as a Counsellor and I have been able to work alongside her and Juniper for Counselling sessions. She is soft, caring, and also intuitive. I am incredibly grateful for her help, as well as Juniper and Barnaby.</p>

  <div class="abs availability-pill">Court Dog Availability</div>
  <div class="abs availability-row row-1">
    <span class="tick"><svg width="11" height="11" viewBox="0 0 20 20"><circle cx="10" cy="10" r="10" fill="#eba35a"/><path d="M5.5 10.5l3 3 6-6.5" fill="none" stroke="#5a1c26" stroke-width="2.2"/></svg>Therapy Dog Visits</span><span class="sep">|</span>
    <span class="tick"><svg width="11" height="11" viewBox="0 0 20 20"><circle cx="10" cy="10" r="10" fill="#eba35a"/><path d="M5.5 10.5l3 3 6-6.5" fill="none" stroke="#5a1c26" stroke-width="2.2"/></svg>Lawyers</span><span class="sep">|</span>
    <span class="tick"><svg width="11" height="11" viewBox="0 0 20 20"><circle cx="10" cy="10" r="10" fill="#eba35a"/><path d="M5.5 10.5l3 3 6-6.5" fill="none" stroke="#5a1c26" stroke-width="2.2"/></svg>Courts</span><span class="sep">|</span>
    <span class="tick"><svg width="11" height="11" viewBox="0 0 20 20"><circle cx="10" cy="10" r="10" fill="#eba35a"/><path d="M5.5 10.5l3 3 6-6.5" fill="none" stroke="#5a1c26" stroke-width="2.2"/></svg>Child Protection</span>
  </div>
  <div class="abs availability-row row-2">
    <span class="tick"><svg width="11" height="11" viewBox="0 0 20 20"><circle cx="10" cy="10" r="10" fill="#eba35a"/><path d="M5.5 10.5l3 3 6-6.5" fill="none" stroke="#5a1c26" stroke-width="2.2"/></svg>Police Station</span><span class="sep">|</span>
    <span class="tick"><svg width="11" height="11" viewBox="0 0 20 20"><circle cx="10" cy="10" r="10" fill="#eba35a"/><path d="M5.5 10.5l3 3 6-6.5" fill="none" stroke="#5a1c26" stroke-width="2.2"/></svg>Ambulance Station</span><span class="sep">|</span>
    <span class="tick"><svg width="11" height="11" viewBox="0 0 20 20"><circle cx="10" cy="10" r="10" fill="#eba35a"/><path d="M5.5 10.5l3 3 6-6.5" fill="none" stroke="#5a1c26" stroke-width="2.2"/></svg>Fire Station</span><span class="sep">|</span>
    <span class="tick"><svg width="11" height="11" viewBox="0 0 20 20"><circle cx="10" cy="10" r="10" fill="#eba35a"/><path d="M5.5 10.5l3 3 6-6.5" fill="none" stroke="#5a1c26" stroke-width="2.2"/></svg>Visits</span>
  </div>

  <div class="abs footer-band"></div>
  <div class="abs rule"></div>
  <div class="abs private-title"><span>Private Therapy Dog Sessions</span></div>
  <div class="abs contact-row contacts-back">
    <span class="ci"><svg width="11" height="11" viewBox="0 0 24 24"><path fill="#fbeee1" d="M6.6 10.8a15 15 0 0 0 6.6 6.6l2.2-2.2c.3-.3.7-.4 1-.2 1.1.4 2.3.6 3.6.6.6 0 1 .4 1 1V20c0 .6-.4 1-1 1A17 17 0 0 1 3 4c0-.6.4-1 1-1h3.5c.6 0 1 .4 1 1 0 1.3.2 2.5.6 3.6.1.3 0 .7-.2 1z"/></svg>0400 123 456</span>
    <span class="ci"><svg width="13" height="10" viewBox="0 0 24 17"><rect x="1" y="1" width="22" height="15" fill="none" stroke="#fbeee1" stroke-width="1.6"/><path d="M1 1l11 9 11-9" fill="none" stroke="#fbeee1" stroke-width="1.6"/></svg>hello@tailsofcomfort.example</span>
    <span class="ci"><svg width="12" height="12" viewBox="0 0 24 24" fill="none" stroke="#fbeee1" stroke-width="1.6"><circle cx="12" cy="12" r="10"/><ellipse cx="12" cy="12" rx="4.5" ry="10"/><path d="M2 12h20M4 6.5h16M4 17.5h16"/></svg>www.tailsofcomfort.example</span>
  </div>
</section>

</body>
</html>
```